Business Card Design

We need a Business card design for our Family Dental Clinic.
Logo design attached.
Colour choices - White, blue and golden to go with the logo.
Business
Contact Information for Business Card
Side 1
DR MARLA FENWICKE
BDS
Suite 6, Level 2, 418 Pembury Street
Carlton North, VIC 3054
Fax : 7264 5039
Email: info@eastbrookvaledentalgroup.com.au
Website: eastbrookvaledentalgroup.com.au
Phone(image) - 7264 5039 (bigger size)
Please make sure that you produce 3 files with the same design
1) As per above
2) With out the Name ( i. e DR Marla Fenwicke BDS)
3) Just the card template (no texts)
Side 2
......................................... at ........................
Please give 24 hours notice if you cannot keep this appointment

```html
<!DOCTYPE html>
<html lang="en">
<head>
<meta charset="utf-8">
<title>Eastbrook Vale Dental Group – Business Card</title>
<link rel="stylesheet" href="https://fonts.googleapis.com/css2?family=Open+Sans:ital,wght@0,400;0,700;1,400&family=Oswald:wght@400&display=swap">
<style>
  :root {
    --white: #ffffff;
    --navy: #1f3f9a;
    --blue: #5a8fd2;
    --blue-deep: #4a7fc6;
    --blue-light: #7ba6dc;
    --wave-1: #eef3fa;
    --wave-2: #d9e5f4;
    --wave-3: #bcd1ec;
    --wave-4: #8fb2e0;
    --gold: #f4c64a;
    --orange: #ef9a2e;
    --ember: #e0622a;
    --text-font: "Open Sans", Arial, sans-serif;
    --figure-font: "Oswald", "Arial Narrow", sans-serif;
  }
  * { margin: 0; padding: 0; box-sizing: border-box; }
  html, body { width: 1200px; height: 972px; overflow: hidden; background: var(--white); }
  .sheet { position: relative; width: 1200px; height: 972px; display: flex; }
  .card { position: relative; width: 600px; height: 972px; overflow: hidden; background: var(--white); font-family: var(--text-font); }
  .card-bg { position: absolute; inset: 0; }

  .brand { position: absolute; left: 0; width: 600px; text-align: center; color: var(--navy); font-family: var(--text-font); font-weight: 700; }
  .brand-dot { display: block; margin: 0 auto 18px; border-radius: 50%; background: var(--navy); }
  .brand-name { display: block; letter-spacing: 1px; line-height: 1.1; }
  .brand-sub { display: block; letter-spacing: 12px; line-height: 1.4; }

  .front .brand { top: 92px; }
  .front .brand-dot { width: 120px; height: 120px; }
  .front .brand-name { font-size: 40px; }
  .front .brand-sub { font-size: 17px; }

  .back .brand { top: 380px; }
  .back .brand-dot { width: 96px; height: 96px; }
  .back .brand-name { font-size: 34px; }
  .back .brand-sub { font-size: 14px; letter-spacing: 10px; }

  .dentist { position: absolute; left: 92px; top: 502px; color: var(--white); font-size: 25px; font-weight: 700; }
  .address { position: absolute; right: 31px; top: 594px; color: var(--white); font-size: 21px; line-height: 36px; text-align: right; font-style: normal; }
  .phone-row { position: absolute; left: 32px; top: 776px; display: flex; align-items: center; gap: 10px; color: var(--white); }
  .phone-row .divider { width: 2px; height: 40px; background: var(--white); }
  .phone-number { font-family: var(--figure-font); font-size: 32px; letter-spacing: 4px; margin-left: 6px; }
  .email-row { position: absolute; left: 32px; top: 864px; display: flex; align-items: center; gap: 22px; color: var(--white); }
  .email { color: var(--white); font-size: 20px; font-style: italic; text-decoration: underline; text-underline-offset: 5px; }
  .website { position: absolute; left: 0; width: 600px; bottom: 6px; text-align: center; color: var(--white); font-size: 19px; }
</style>
</head>
<body>
<div class="sheet">

  <section class="card front">
    <svg class="card-bg" width="600" height="972" viewBox="0 0 600 972">
      <defs>
        <linearGradient id="frontBlue" x1="0" y1="0" x2="1" y2="1">
          <stop offset="0" stop-color="var(--blue-deep)"/>
          <stop offset="1" stop-color="var(--blue)"/>
        </linearGradient>
      </defs>
      <path d="M0 372 Q300 430 600 372 L600 972 L0 972 Z" fill="var(--blue-light)"/>
      <path d="M0 392 Q300 445 600 392 L600 972 L0 972 Z" fill="url(#frontBlue)"/>
      <rect x="0" y="917" width="600" height="14" fill="var(--gold)"/>
      <rect x="0" y="931" width="600" height="14" fill="var(--orange)"/>
      <rect x="0" y="945" width="600" height="27" fill="var(--ember)"/>
    </svg>

    <div class="brand">
      <span class="brand-dot"></span>
      <span class="brand-name">EASTBROOK VALE</span>
      <span class="brand-sub">DENTAL GROUP</span>
    </div>

    <p class="dentist">Dr&nbsp; MARLA FENWICKE BDS</p>
    <address class="address">
      418 Pembury Street Carlton North<br>
      Suite 6, Level 2<br>
      VIC 3054
    </address>

    <div class="phone-row">
      <svg width="34" height="30" viewBox="0 0 34 30" fill="none" stroke="var(--white)" stroke-width="2" aria-label="Fax">
        <rect x="8" y="2" width="18" height="9"/>
        <rect x="2" y="11" width="30" height="14" rx="3"/>
        <rect x="8" y="20" width="18" height="8" fill="var(--blue-deep)"/>
      </svg>
      <span class="divider"></span>
      <svg width="26" height="30" viewBox="0 0 26 30" aria-label="Phone">
        <path d="M6 2 L11 2 L13 9 L9 12 Q12 19 16 22 L19 18 L25 21 L24 27 Q16 30 9 22 Q2 13 6 2 Z" fill="var(--white)"/>
      </svg>
      <span class="phone-number">:&nbsp; 7264 5039</span>
    </div>

    <div class="email-row">
      <svg width="42" height="30" viewBox="0 0 42 30" fill="none" stroke="var(--white)" stroke-width="2" aria-label="Email">
        <rect x="1" y="1" width="40" height="28"/>
        <path d="M1 1 L21 17 L41 1 M1 29 L16 13 M41 29 L26 13"/>
      </svg>
      <span class="email">info@eastbrookvaledentalgroup.com.au</span>
    </div>

    <p class="website">www.eastbrookvaledentalgroup.com.au</p>
  </section>

  <section class="card back">
    <svg class="card-bg" width="600" height="972" viewBox="0 0 600 972">
      <path d="M0 800 Q300 700 600 760 L600 972 L0 972 Z" fill="var(--wave-1)"/>
      <path d="M0 838 Q300 748 600 800 L600 972 L0 972 Z" fill="var(--wave-2)"/>
      <path d="M0 878 Q300 800 600 846 L600 972 L0 972 Z" fill="var(--wave-3)"/>
      <path d="M0 920 Q300 856 600 896 L600 972 L0 972 Z" fill="var(--wave-4)"/>
      <path d="M0 958 Q300 905 600 940 L600 972 L0 972 Z" fill="var(--blue)"/>
    </svg>

    <div class="brand">
      <span class="brand-dot"></span>
      <span class="brand-name">EASTBROOK VALE</span>
      <span class="brand-sub">DENTAL GROUP</span>
    </div>
  </section>

</div>
</body>
</html>
```